WP website design (N Kentucky)

We need a wordpress design that will incorporate a professional color scheme with company logo in a clean layout. The design needs to consider that this will be developed on a responsive theme. Colors are undetermined - can use a dark red - logo is black so creative use of colors will be important. Client wants a 'modern' look.
Updates

Project Deadline Extended
Reason: Client wants a few more designs

Industry/Entity Type

It Company

Font styles to use
Serif
Sans Serif

Requirements
Must have
• Must Have:
- Navigation: 1) Home 2) Auctions 3) Auction Marketing 4) Buying at Auction 5) About Us 6) Contact Us

Site will have a slideshow element and the following widgets: 1) Featured Auctions 2) Testimonials blog widget 3) 'Auction Alerts' email sign up 4) Fz Chirpa Zelnix+ icons. Colors can be the meadowline7 gold/black from http://www.brambleridgehouses.example/

In the footer, there will be smaller company logo, the affiliations logo, and contact info below:
Copperfield Gavel Sales, LLC / Wes Pellham
email: wespell@mailbox.example; wes.pellham@ml7.example
phone: (859) 555-0147 mobile phone: (859)555-0182
Domain: http://www.copperfieldgavelsales.example/
Nice to have
• - - Site will have drop-down menus - please indicate the styling, for instance the dropdown menus 1) Upcoming Auctions 2) Past Auctions under the 'Auctions' link

```html
<!DOCTYPE html>
<html lang="en">
<head>
<meta charset="utf-8">
<title>Copperfield Gavel Sales, LLC</title>
<link href="https://fonts.googleapis.com/css2?family=Open+Sans:wght@400;600;700&family=Oswald:wght@400;500&display=swap" rel="stylesheet">
<style>
:root{
  --red:#b3161b;
  --red-dark:#8c0f13;
  --ink:#1c1c1c;
  --charcoal:#2a2a2a;
  --panel:#3a3a3a;
  --grey-light:#e4e4e4;
  --grey-mid:#cfcfcf;
  --text:#555;
  --white:#fff;
}
*{box-sizing:border-box;margin:0;padding:0}
html,body{width:711px;height:1200px;overflow:hidden}
body{font-family:"Open Sans",Arial,sans-serif;color:var(--text);background:var(--grey-light);font-size:8px;line-height:1.45}
.site{width:711px;height:1200px;position:relative}

/* header */
.site-header{height:70px;background:linear-gradient(#2e2e2e,#151515);display:flex;align-items:center;padding:0 22px 0 82px}
.brand{width:168px;height:50px;background:var(--white);display:flex;align-items:center;gap:8px;padding:0 10px;border:1px solid #999}
.brand-mark{width:16px;height:16px;background:var(--ink);flex:none}
.brand-name{font-weight:700;font-size:10px;color:var(--ink);line-height:1.15}
.main-nav{margin-left:auto;display:flex;height:70px}
.main-nav a{color:#ddd;text-decoration:none;font-size:7.5px;text-transform:uppercase;display:flex;align-items:center;padding:0 9px}
.main-nav a.active{background:var(--red);color:var(--white)}

/* hero */
.hero{height:415px;position:relative;background:#9aa3ab}
.hero-photo{position:absolute;inset:0;background:linear-gradient(180deg,#5e6870 0%,#aeb7be 40%,#d5d9dc 62%,#7c7f82 100%)}
.hero-tagline{position:absolute;left:0;right:0;top:250px;height:42px;background:rgba(20,20,20,.55);text-align:right;padding:6px 40px 0 0;color:var(--white)}
.hero-tagline h2{font-family:"Oswald",Arial,sans-serif;font-weight:400;font-size:14px;letter-spacing:.5px}
.hero-tagline p{font-size:8px;color:#ddd}
.categories{position:absolute;top:358px;left:82px;right:82px;display:flex;gap:10px}
.category{flex:1;height:42px;background:rgba(30,30,30,.9);display:flex;align-items:center;gap:10px;padding:0 12px;color:var(--white);font-size:11px;line-height:1.15}
.category-icon{width:20px;height:20px;background:var(--red);flex:none;display:flex;align-items:center;justify-content:center}

/* welcome */
.welcome{height:145px;padding:14px 82px 0;display:flex;gap:28px;background:var(--grey-light)}
.welcome-text{flex:1}
.welcome h1{font-size:11px;font-weight:600;color:var(--ink);margin-bottom:6px}
.welcome h1 span,.hl{color:var(--red)}
.welcome p{margin-bottom:8px}
.read-more{color:var(--red);font-weight:700;font-size:7px;text-transform:uppercase}
.alerts-signup{width:150px}
.alerts-signup h3{font-size:11px;font-weight:600;color:var(--ink);margin-bottom:4px}
.alerts-signup input{display:block;width:100%;height:16px;border:1px solid var(--grey-mid);font:7px "Open Sans",sans-serif;padding:0 4px;margin:6px 0}
.btn{display:inline-block;background:var(--red);color:var(--white);font-size:7px;padding:3px 8px;font-weight:600;text-transform:uppercase}

/* features band */
.features{height:145px;background:#111 linear-gradient(#1b1b1b,#050505);display:flex;justify-content:center;gap:14px;padding-top:20px}
.feature-card{width:176px;height:110px;background:var(--panel);position:relative;padding:24px 12px 0;color:#ccc;text-align:center}
.feature-icon{position:absolute;top:-12px;left:50%;margin-left:-13px;width:26px;height:26px;border-radius:50%;background:var(--red);border:2px solid #555;display:flex;align-items:center;justify-content:center}
.feature-card h3{font-size:11px;font-weight:600;color:var(--white);margin-bottom:4px;text-align:left}
.feature-card p{font-size:6.5px;text-align:left;margin-bottom:6px}

/* news */
.news-row{height:185px;background:var(--grey-light);padding:16px 82px 0;display:flex;gap:26px}
.column{flex:1}
.column h2{font-size:12px;font-weight:600;color:var(--ink);border-bottom:1px solid var(--grey-mid);padding-bottom:4px;margin-bottom:8px}
.news-item{display:flex;gap:8px;margin-bottom:10px}
.date{width:26px;height:28px;background:var(--red);color:var(--white);text-align:center;font-weight:700;font-size:8px;line-height:1.1;padding-top:3px;flex:none}
.date b{display:block;font-size:10px}
.news-item h4{font-size:7.5px;color:var(--red);font-weight:600}
.testimonials{display:flex;gap:12px}
.testimonial{flex:1;font-size:6.5px}
.testimonial-head{display:flex;align-items:center;gap:6px;margin-bottom:4px}
.avatar{width:28px;height:28px;border-radius:50%;background:#bbb;border:2px solid var(--white);flex:none}
.testimonial-head b{color:var(--red);display:block;font-size:7px}

/* featured */
.featured{height:105px;background:#d9d9d9;position:relative;padding-top:24px}
.ribbon{position:absolute;top:0;left:50%;transform:translateX(-50%);background:var(--red);color:var(--white);font-size:11px;font-weight:600;padding:3px 26px}
.carousel{display:flex;align-items:center;justify-content:center;gap:6px}
.arrow{width:16px;height:52px;background:var(--white);display:flex;align-items:center;justify-content:center}
.slide{width:120px;height:64px;border:2px solid var(--white);background:linear-gradient(#6f8ba6,#cdd6de 60%,#7a7c80)}

/* footer */
.site-footer{height:135px;background:var(--charcoal);color:#bbb;padding:14px 82px 0;display:flex;gap:30px;font-size:7px}
.site-footer h4{color:var(--white);font-size:8px;font-weight:600;margin-bottom:5px}
.quick-links{width:90px;list-style:none}
.quick-links li{line-height:1.7}
.contact-line{display:flex;align-items:center;gap:5px;line-height:1.9}
.contact-line svg{flex:none}
.footer-brand{margin-left:auto;width:150px}
.footer-logo{background:var(--white);height:36px;display:flex;align-items:center;gap:6px;padding:0 8px;margin-bottom:10px}
.footer-logo .brand-name{font-size:8px}
.socials{display:flex;gap:6px;align-items:center}
.social{width:16px;height:16px;background:#555}
.affiliation{width:26px;height:26px;border-radius:50%;background:#777;margin-left:6px}
</style>
</head>
<body>
<div class="site">
  <header class="site-header">
    <div class="brand"><span class="brand-mark"></span><span class="brand-name">Copperfield Gavel Sales, LLC</span></div>
    <nav class="main-nav">
      <a class="active">Home</a><a>Auctions</a><a>Auction Marketing</a><a>Buying at Auction</a><a>About Us</a><a>Contact Us</a>
    </nav>
  </header>

  <section class="hero">
    <div class="hero-photo" role="img" aria-label="Slideshow photo of a modern glass high-rise office building"></div>
    <div class="hero-tagline">
      <h2>SUPERBLY LOCATED, INTRINSICALLY READY TO ENJOY</h2>
      <p>482 ALDER CREST ROAD, MIDLANDS</p>
    </div>
    <div class="categories">
      <div class="category"><span class="category-icon"><svg width="10" height="12" viewBox="0 0 10 12"><rect x="1" y="1" width="8" height="11" fill="#fff"/><g fill="#b3161b"><rect x="3" y="3" width="1.5" height="1.5"/><rect x="5.5" y="3" width="1.5" height="1.5"/><rect x="3" y="6" width="1.5" height="1.5"/><rect x="5.5" y="6" width="1.5" height="1.5"/></g></svg></span>High Rises</div>
      <div class="category"><span class="category-icon"><svg width="12" height="11" viewBox="0 0 12 11"><path d="M6 0L12 3H0z M1 4h2v5H1z M5 4h2v5H5z M9 4h2v5H9z M0 9.5h12V11H0z" fill="#fff"/></svg></span>Government Office Buildings</div>
      <div class="category"><span class="category-icon"><svg width="12" height="11" viewBox="0 0 12 11"><path d="M6 0L12 5H10V11H2V5H0z" fill="#fff"/></svg></span>Apartment Communities</div>
    </div>
  </section>

  <section class="welcome">
    <div class="welcome-text">
      <h1>Welcome to <span>Copperfield Gavel Sales, LLC</span></h1>
      <p>Our auction team markets commercial and residential property across the region with care. Every sale is planned, promoted and run by people who know the local market and the buyers in it.</p>
      <p>Browse current listings, register to bid, or contact us for a free property review.</p>
      <span class="read-more">Read More</span>
    </div>
    <div class="alerts-signup">
      <h3>Auction <span class="hl">Alerts</span></h3>
      <p>Enter your email to get notice of new auctions first.</p>
      <input type="text" value="Email address" aria-label="Email address">
      <span class="btn">Subscribe</span>
    </div>
  </section>

  <section class="features">
    <article class="feature-card">
      <span class="feature-icon"><svg width="12" height="12" viewBox="0 0 12 12"><path d="M6 1l1.5 3.3 3.5.4-2.6 2.4.7 3.5L6 8.8 2.9 10.6l.7-3.5L1 4.7l3.5-.4z" fill="#fff"/></svg></span>
      <h3>Featured <span class="hl">Auctions</span></h3>
      <p>See the properties heading to the block this season, with photos, terms and dates for every sale we run.</p>
      <span class="btn">Read More</span>
    </article>
    <article class="feature-card">
      <span class="feature-icon"><svg width="12" height="12" viewBox="0 0 12 12"><circle cx="6" cy="4" r="2.5" fill="#fff"/><path d="M1.5 11c0-3 2-4.5 4.5-4.5s4.5 1.5 4.5 4.5z" fill="#fff"/></svg></span>
      <h3>Client <span class="hl">Testimonials</span></h3>
      <p>Read what sellers and buyers say about working with our team from the first call through closing day.</p>
      <span class="btn">Read More</span>
    </article>
    <article class="feature-card">
      <span class="feature-icon"><svg width="12" height="12" viewBox="0 0 12 12"><path d="M1 3h10v7H1z" fill="#fff"/><path d="M1 3l5 4 5-4" stroke="#b3161b" fill="none"/></svg></span>
      <h3>Auction <span class="hl">Alerts</span></h3>
      <p>Sign up once and we will send new auction dates, property details and bidding news straight to you.</p>
      <span class="btn">Read More</span>
    </article>
  </section>

  <section class="news-row">
    <div class="column">
      <h2>Latest <span class="hl">News</span></h2>
      <div class="news-item"><span class="date"><b>18</b>JAN</span><div><h4>New office tower listed for spring sale</h4><p>Bidding opens next month on a twelve storey tower near the river district.</p></div></div>
      <div class="news-item"><span class="date"><b>24</b>JAN</span><div><h4>Apartment block sells above reserve price</h4><p>Forty units found a new owner after a busy morning of floor bidding.</p></div></div>
      <span class="read-more">Read More</span>
    </div>
    <div class="column">
      <h2>Clients <span class="hl">Testimonials</span></h2>
      <div class="testimonials">
        <div class="testimonial"><div class="testimonial-head"><span class="avatar" role="img" aria-label="Client portrait"></span><span><b>Lena Morrow</b>Property Owner</span></div><p>The team sold our building in one day and handled every detail with care.</p></div>
        <div class="testimonial"><div class="testimonial-head"><span class="avatar" role="img" aria-label="Client portrait"></span><span><b>Ross Talbot</b>Investor</span></div><p>Clear terms, honest advice and a fair sale from start to finish.</p></div>
      </div>
    </div>
  </section>

  <section class="featured">
    <h2 class="ribbon">Featured Auctions</h2>
    <div class="carousel">
      <span class="arrow"><svg width="6" height="10" viewBox="0 0 6 10"><path d="M5 1L1 5l4 4" stroke="#333" stroke-width="1.5" fill="none"/></svg></span>
      <div class="slide" role="img" aria-label="Photo of an auction property: office tower"></div>
      <div class="slide" role="img" aria-label="Photo of an auction property: glass office building"></div>
      <div class="slide" role="img" aria-label="Photo of an auction property: high-rise at dusk"></div>
      <div class="slide" role="img" aria-label="Photo of an auction property: city block"></div>
      <span class="arrow"><svg width="6" height="10" viewBox="0 0 6 10"><path d="M1 1l4 4-4 4" stroke="#333" stroke-width="1.5" fill="none"/></svg></span>
    </div>
  </section>

  <footer class="site-footer">
    <div>
      <h4>Quick Links</h4>
      <ul class="quick-links"><li>Home</li><li>Company</li><li>Development</li><li>Staff</li><li>Contact</li></ul>
    </div>
    <div>
      <h4>Contact Information</h4>
      <div class="contact-line"><svg width="8" height="8" viewBox="0 0 8 8"><circle cx="4" cy="3" r="2" fill="#b3161b"/><path d="M1 8c0-2 1.5-3 3-3s3 1 3 3z" fill="#b3161b"/></svg>Copperfield Gavel Sales, LLC / Wes Pellham</div>
      <div class="contact-line"><svg width="8" height="8" viewBox="0 0 8 8"><path d="M0 1.5h8v5H0z" fill="#b3161b"/></svg>wespell@mailbox.example</div>
      <div class="contact-line"><svg width="8" height="8" viewBox="0 0 8 8"><path d="M0 1.5h8v5H0z" fill="#b3161b"/></svg>wes.pellham@ml7.example</div>
      <div class="contact-line"><svg width="8" height="8" viewBox="0 0 8 8"><path d="M2 0l1.5 2-1 1a4 4 0 0 0 2.5 2.5l1-1 2 1.5-1 2C3 8 0 5 0 1z" fill="#b3161b"/></svg>(859) 555-0147</div>
      <div class="contact-line"><svg width="8" height="8" viewBox="0 0 8 8"><rect x="2" y="0" width="4" height="8" rx="1" fill="#b3161b"/></svg>(859)555-0182</div>
    </div>
    <div class="footer-brand">
      <div class="footer-logo"><span class="brand-mark"></span><span class="brand-name">Copperfield Gavel Sales, LLC</span></div>
      <div class="socials"><span class="social" aria-label="Fz"></span><span class="social" aria-label="Chirpa"></span><span class="social" aria-label="Zelnix+"></span><span class="affiliation" aria-label="Affiliation badge"></span></div>
    </div>
  </footer>
</div>
</body>
</html>
```